Banner Design for High End Jewelry Website

We need a banner for our website (brivela.com) for a sale that we will be running. The banner should be a size 1187 × 400. I have included a few pieces of jewelry to be included in the banner (do not need to use all, can use just some). The banner should say:
"Christmas is Closer Than You Think Sale!"
Shop Now

Industry/Entity Type

Jewelry

```html
<!DOCTYPE html>
<html lang="en">
<head>
<meta charset="utf-8">
<title>Brivela Christmas Sale Banner</title>
<link rel="stylesheet" href="https://fonts.googleapis.com/css2?family=Damion&family=Montserrat:wght@400;500&display=swap">
<style>
  :root {
    --ink: #111111;
    --white: #ffffff;
    --sale-red: #ec1c24;
    --star-gold: #d9a33a;
    --bg-light: #fbfbfb;
    --bg-mid: #e4e4e4;
    --gold-hi: #ecc85a;
    --gold-mid: #d9aa3c;
    --gold-lo: #b98a22;
    --antique: #8c8068;
  }
  * { margin: 0; padding: 0; box-sizing: border-box; }
  html, body { width: 1200px; height: 404px; overflow: hidden; background: var(--white); }
  .banner {
    position: relative;
    width: 1200px;
    height: 404px;
    overflow: hidden;
    font-family: "Montserrat", sans-serif;
  }
  .backdrop {
    position: absolute; inset: 0;
    background:
      radial-gradient(ellipse 520px 260px at 330px 120px, var(--bg-light) 0%, rgba(251,251,251,0) 70%),
      radial-gradient(ellipse 700px 300px at 900px 260px, rgba(220,220,220,0.8) 0%, rgba(220,220,220,0) 70%),
      linear-gradient(135deg, var(--bg-light) 0%, var(--bg-mid) 55%, var(--bg-light) 100%);
  }
  .headline {
    position: absolute;
    left: 48px; top: 36px;
    font-family: "Damion", cursive;
    font-size: 70px;
    font-weight: 400;
    line-height: 1;
    color: var(--ink);
    letter-spacing: -1px;
  }
  .spark { position: absolute; }
  .subline {
    position: absolute;
    left: 56px; top: 133px;
    font-size: 19px;
    font-weight: 500;
    color: var(--ink);
    letter-spacing: 0.2px;
  }
  .sale-band {
    position: absolute;
    left: 0; top: 167px;
    width: 298px; height: 60px;
    background: var(--sale-red);
  }
  .sale-band span {
    position: absolute;
    left: 97px; top: 8px;
    font-size: 38px;
    font-weight: 400;
    color: var(--white);
    letter-spacing: 20px;
  }
  .shop-button {
    position: absolute;
    left: 494px; top: 325px;
    width: 199px; height: 51px;
    background: var(--ink);
    color: var(--white);
    font-size: 13px;
    letter-spacing: 4px;
    display: flex; align-items: center; justify-content: center;
    text-decoration: none;
  }
  .jewel { position: absolute; }
  .jewel-bracelet {
    left: 918px; top: 140px; width: 270px; height: 246px;
    border-radius: 46% 38% 40% 46% / 50% 44% 46% 50%;
    background: linear-gradient(160deg, var(--gold-hi) 0%, var(--gold-mid) 55%, var(--gold-lo) 100%);
  }
  .jewel-brooch {
    left: 808px; top: 98px; width: 166px; height: 148px;
    border-radius: 50%;
    background: radial-gradient(circle at 50% 50%, var(--gold-hi) 0%, var(--gold-mid) 50%, var(--antique) 100%);
  }
  .jewel-earrings {
    left: 990px; top: 6px; width: 140px; height: 146px;
    border-radius: 40%;
    background: linear-gradient(150deg, var(--gold-hi) 0%, var(--gold-mid) 60%, var(--gold-lo) 100%);
  }
  .jewel-ring {
    left: 770px; top: 256px; width: 146px; height: 140px;
    border-radius: 45%;
    background: linear-gradient(150deg, #7a9a76 0%, #6a6a80 45%, var(--gold-mid) 100%);
  }
</style>
</head>
<body>
  <main class="banner">
    <div class="backdrop" role="img" aria-label="Soft silver and white background with faint star and swirling light streaks"></div>

    <h1 class="headline">Christmas</h1>
    <svg class="spark" style="left:232px;top:30px" width="30" height="30" viewBox="0 0 30 30" aria-hidden="true">
      <path d="M15 0 L17 13 L30 15 L17 17 L15 30 L13 17 L0 15 L13 13 Z" fill="var(--star-gold)"/>
    </svg>
    <svg class="spark" style="left:127px;top:63px" width="18" height="18" viewBox="0 0 30 30" aria-hidden="true">
      <path d="M15 0 L17 13 L30 15 L17 17 L15 30 L13 17 L0 15 L13 13 Z" fill="var(--star-gold)"/>
    </svg>
    <svg class="spark" style="left:284px;top:111px" width="16" height="16" viewBox="0 0 30 30" aria-hidden="true">
      <path d="M15 0 L17 13 L30 15 L17 17 L15 30 L13 17 L0 15 L13 13 Z" fill="var(--star-gold)"/>
    </svg>

    <p class="subline">is Closer Than You Think</p>
    <div class="sale-band"><span>SALE</span></div>

    <a class="shop-button" href="#">SHOP NOW</a>

    <div class="jewel jewel-bracelet" role="img" aria-label="Photo of a wide gold scale-pattern cuff bracelet set with diamonds"></div>
    <div class="jewel jewel-brooch" role="img" aria-label="Photo of a round gold flower brooch with a ruby centre and diamonds"></div>
    <div class="jewel jewel-earrings" role="img" aria-label="Photo of gold earrings with emerald and ruby cabochons and diamonds"></div>
    <div class="jewel jewel-ring" role="img" aria-label="Photo of a gold ring cluster set with coloured cabochon stones"></div>
  </main>
</body>
</html>
```